Etiketten für Kuchen im Glas
Zielgruppe
Die Firma Brelkat bietet kulinarische Präsente und Geschenkideen zum Thema kreatives Backen an. Unsere Zielgruppe ist B2C und Werbetreibende, die unsere Produkte als Geschenke einsetzen.
Aufgabenstellung
Für unsere Zielgruppe "Feinkostläden" benötigen wir ein etwas edleres klasssisches Etiketten-Design.
Gestaltet wird der Deckel und die Vorderseite eines Etiketts für ein 290 ml FUMS-Glas. Die entsprechende Designvorlage steht hier zum Download bereit:
https://files.tralvex-speicher.de/u/4827351/7902_01358_0000-Vorlage%20CMYK%20v08_2013-09.psd
Benötigt werden 4 unterschiedliche Etiketten, die aber aus einem "Guss" sein sollten für die Sorten: Stracciatella, Schokolade, Zitrone, Stollen. Die Sorte sollte mit auf dem Etikett stehen.
Sonstige Angaben auf dem Etikett:
- optional "Kuchen im Glas"
- gerne Grünhof Logo (siehe Anhang)
- optional "fertig gebacken". Könnte z.B. gut auf dem Deckel in Kombination mit "Kuchen im Gla" stehen
Achtung: Das Etikett für die Rückseite mit Deklaration muss nicht gestaltet werden.
Tipps: Das Etikett ist konisch und das Glas rund. Das bedeutet, dass Bilder + Schriften mit einer leichten Wölbung kreiert werden sollten. Für die Wölbung kann man sich gut an der unteren Designlinie orientieren.
Farbgestaltung: eher dunkel; z.B. Grau, Dunkelblau evtl. Schwarz
Schriften: Es dürfen auch kostenpflichtige Schriften verwendet werden. Freie Schriften allerdings bevorzugt
Format: Photoshop PSD inklusive allen Ebenen und verwendeten Elementen als einzelne Ebene.
Bei Fragen gerne melden, ich freue mich auf Eure Designs.

```html
<!DOCTYPE html>
<html lang="de">
<head>
<meta charset="utf-8">
<title>Kuchen im Glas – Stracciatella Etiketten</title>
<link rel="stylesheet" href="https://fonts.googleapis.com/css2?family=Great+Vibes&family=Pinyon+Script&family=Libre+Baskerville:ital,wght@0,400;1,400&display=swap">
<style>
  :root {
    --bg: #ffffff;
    --label-black: #1b1b1b;
    --label-edge: #0e0e0e;
    --frame-grey: #6f6f70;
    --title-white: #ffffff;
    --variety-grey: #8e8b84;
    --brand-dot: #8e8b84;
    --cake-light: #e6c99a;
    --cake-crust: #b98447;
  }
  html, body {
    margin: 0;
    padding: 0;
    width: 1128px;
    height: 1200px;
    overflow: hidden;
    background: var(--bg);
  }
  .sheet { display: block; width: 1128px; height: 1200px; }
  .label-body { fill: var(--label-black); stroke: var(--label-edge); stroke-width: 4; }
  .label-frame { fill: none; stroke: var(--frame-grey); stroke-width: 3; }
  .variety { font-family: "Pinyon Script", cursive; fill: var(--variety-grey); }
  .title { font-family: "Great Vibes", cursive; fill: var(--title-white); }
  .tagline { font-family: "Libre Baskerville", serif; font-style: italic; fill: var(--title-white); }
  .brand-dot { fill: var(--brand-dot); }
  .brand-name { font-family: "Libre Baskerville", serif; font-weight: 400; fill: var(--title-white); }
</style>
</head>
<body>
<svg class="sheet" viewBox="0 0 1128 1200" xmlns="http://www.w3.org/2000/svg">
  <defs>
    <radialGradient id="cakeTone" cx="45%" cy="45%" r="65%">
      <stop offset="0%" stop-color="var(--cake-light)"/>
      <stop offset="100%" stop-color="var(--cake-crust)"/>
    </radialGradient>
    <radialGradient id="labelGlow" cx="50%" cy="45%" r="60%">
      <stop offset="0%" stop-color="#262626"/>
      <stop offset="100%" stop-color="#161616"/>
    </radialGradient>
    <clipPath id="lidClip"><circle cx="564" cy="304" r="244"/></clipPath>
    <clipPath id="frontClip"><path d="M76 738 Q564 636 1052 738 L988 1098 Q564 1046 140 1098 Z"/></clipPath>
  </defs>

  <!-- Deckel -->
  <g class="lid">
    <circle class="label-body" cx="564" cy="304" r="256" fill="url(#labelGlow)"/>
    <circle class="label-frame" cx="564" cy="304" r="244"/>
    <g class="brand">
      <circle class="brand-dot" cx="530" cy="100" r="4"/>
      <text class="brand-name" x="540" y="105" font-size="14">Grünhof</text>
    </g>
    <text class="variety" x="564" y="168" font-size="38" text-anchor="middle">-Stracciatella-</text>
    <text class="title" x="378" y="268" font-size="88">Kuchen</text>
    <text class="title" x="518" y="336" font-size="60">im</text>
    <text class="title" x="612" y="346" font-size="92">Glas</text>
    <text class="tagline" x="392" y="306" font-size="15">… fertig</text>
    <text class="tagline" x="404" y="325" font-size="15">gebacken.</text>
    <g clip-path="url(#lidClip)">
      <path role="img" aria-label="Foto: drei Scheiben Stracciatella-Rührkuchen mit Schokostückchen"
            d="M408 545 Q405 430 470 392 Q540 360 600 372 Q662 385 668 450 Q672 500 660 545 Z"
            fill="url(#cakeTone)"/>
    </g>
  </g>

  <!-- Vorderseite, konisch -->
  <g class="front">
    <path class="label-body" fill="url(#labelGlow)" stroke-linejoin="round"
          d="M54 722 Q564 614 1074 722 L1006 1122 Q564 1068 122 1122 Z"/>
    <path class="label-frame" d="M76 738 Q564 636 1052 738 L988 1098 Q564 1046 140 1098 Z"/>
    <text class="variety" x="565" y="748" font-size="38" text-anchor="middle">-Stracciatella-</text>
    <g class="brand">
      <circle class="brand-dot" cx="858" cy="768" r="5"/>
      <text class="brand-name" x="870" y="774" font-size="18">Grünhof</text>
    </g>
    <text class="title" x="300" y="836" font-size="96">Kuchen</text>
    <text class="title" x="498" y="896" font-size="64">im</text>
    <text class="title" x="604" y="906" font-size="100">Glas</text>
    <text class="tagline" x="298" y="904" font-size="17" transform="rotate(-8 298 904)">… fertig gebacken.</text>
    <g clip-path="url(#frontClip)">
      <path role="img" aria-label="Foto: drei Scheiben Stracciatella-Rührkuchen mit Schokostückchen"
            d="M400 1090 Q398 965 460 930 Q540 900 620 912 Q712 925 728 990 Q736 1040 724 1090 Z"
            fill="url(#cakeTone)"/>
    </g>
  </g>
</svg>
</body>
</html>
```